business card design for a plumbing contractor

i need a double business card for a plumbing business, our initial service is residential Sewer Drain Cleaning.

Target Market(s)

other plumbing Business

Industry/Entity Type

Plumbing

Contact Information for Business Card

www.PipeworksTopNotch.example- 5173829046-

Font styles to use
Serif

Colors
ec1f27
0455a3

```html
<!DOCTYPE html>
<html lang="en">
<head>
<meta charset="utf-8">
<title>Pipeworks Top Notch – Business Card</title>
<link href="https://fonts.googleapis.com/css2?family=Roboto:wght@300;400;500;700&display=swap" rel="stylesheet">
<style>
  :root {
    --bg: #e9e7e4;
    --card-dark: #3b3b3d;
    --card-light: #ffffff;
    --red: #e0282a;
    --grey: #7a746c;
    --text: #6d6760;
    --white: #ffffff;
  }
  * { margin: 0; padding: 0; box-sizing: border-box; }
  html, body { width: 1200px; height: 930px; overflow: hidden; }
  body {
    background: var(--bg);
    font-family: "Roboto", sans-serif;
    position: relative;
  }
  .card {
    position: absolute;
    width: 640px;
    height: 366px;
    border-radius: 16px;
    overflow: hidden;
    box-shadow: 0 6px 18px rgba(0,0,0,0.18);
  }
  .card--back { left: 280px; top: 52px; background: var(--card-dark); }
  .card--front { left: 280px; top: 478px; background: var(--card-light); }

  .brand {
    position: absolute;
    display: flex;
    align-items: center;
    gap: 12px;
    font-weight: 700;
    line-height: 1.05;
  }
  .brand__mark { width: 22px; height: 22px; background: var(--red); flex: none; }
  .brand__name { font-size: 34px; }
  .card--back .brand { left: 50%; top: 50%; transform: translate(-50%, -50%); }
  .card--back .brand__name { color: var(--white); }
  .card--front .brand { left: 44px; top: 52px; }
  .card--front .brand__name { color: var(--grey); font-size: 30px; }

  .person { position: absolute; right: 40px; top: 118px; text-align: right; }
  .person__name { color: var(--red); font-size: 30px; font-weight: 400; letter-spacing: 0.5px; }
  .person__role { color: var(--text); font-size: 15px; font-weight: 300; margin-top: 2px; }

  .divider {
    position: absolute; left: 40px; right: 40px; top: 196px;
    height: 1px; background: var(--red);
  }

  .services {
    position: absolute; right: 36px; top: 212px;
    list-style: none; text-align: right;
    color: var(--text); font-size: 15px; font-weight: 300; line-height: 22px;
  }
  .services li::after {
    content: ""; display: inline-block; width: 7px; height: 7px;
    border-radius: 50%; background: var(--red); margin-left: 10px; vertical-align: middle;
  }

  .contacts {
    position: absolute; left: 44px; top: 212px;
    list-style: none; color: var(--text); font-size: 15px; font-weight: 300; line-height: 22px;
  }
  .contacts li { display: flex; align-items: center; gap: 10px; }
  .contacts svg { width: 12px; height: 12px; flex: none; }

  .footer-wave { position: absolute; left: 0; bottom: 0; width: 640px; height: 80px; }
</style>
</head>
<body>

<section class="card card--back" aria-label="Card back">
  <div class="brand">
    <span class="brand__name">Pipeworks Top Notch</span>
    <span class="brand__mark"></span>
  </div>
</section>

<section class="card card--front" aria-label="Card front">
  <div class="brand">
    <span class="brand__name">Pipeworks<br>Top Notch</span>
    <span class="brand__mark"></span>
  </div>

  <div class="person">
    <div class="person__name">DANIEL HARPER</div>
    <div class="person__role">Director</div>
  </div>

  <div class="divider"></div>

  <ul class="contacts">
    <li>
      <svg viewBox="0 0 12 12"><path d="M2 1l2 0 1 3-1.5 1a6 6 0 0 0 3.5 3.5L8 7l3 1v2a1 1 0 0 1-1 1A9 9 0 0 1 1 2a1 1 0 0 1 1-1z" fill="var(--red)"/></svg>
      5173829046
    </li>
    <li>
      <svg viewBox="0 0 12 12"><rect x="1" y="2.5" width="10" height="7" fill="none" stroke="var(--red)" stroke-width="1.2"/><path d="M1 2.5l5 4 5-4" fill="none" stroke="var(--red)" stroke-width="1.2"/></svg>
      Dispatcher@PipeworksTopNotch.example
    </li>
    <li>
      <svg viewBox="0 0 12 12"><circle cx="6" cy="6" r="5" fill="none" stroke="var(--red)" stroke-width="1.2"/><path d="M1 6h10M6 1c2.5 2.5 2.5 7.5 0 10M6 1c-2.5 2.5-2.5 7.5 0 10" fill="none" stroke="var(--red)" stroke-width="1"/></svg>
      www.PipeworksTopNotch.example
    </li>
  </ul>

  <ul class="services">
    <li>Sewer Drain Cleaning</li>
    <li>Maintenance</li>
    <li>Trenchless Pipe Installs</li>
  </ul>

  <svg class="footer-wave" viewBox="0 0 640 80" preserveAspectRatio="none" aria-hidden="true">
    <path d="M0 64 L390 64 C420 64 430 50 450 50 L640 50 L640 58 L456 58 C436 58 428 70 396 70 L0 70 Z" fill="var(--grey)"/>
    <path d="M0 72 L410 72 C450 72 460 20 520 20 L640 20 L640 80 L0 80 Z" fill="var(--red)"/>
  </svg>
</section>

</body>
</html>
```